Brightwell Circle OKAV: Global Policy to Local Action

We need two professional visuals that represent the vision and strategy of the organization. I attached two rough images of the first visual and one image of the second visual. I also attached a pdf of the narrative to give context for each visual.

Target Market(s)

Global Health Policy Makers

Colors
ec1f27

Requirements
Must have
• Two separate images representing the flow of the work

```html
<!DOCTYPE html>
<html lang="en">
<head>
<meta charset="utf-8">
<title>Brightwell Circle OKAV: Global Policy to Local Action</title>
<link href="https://fonts.googleapis.com/css2?family=Arimo:ital,wght@0,700;1,700&family=Nunito+Sans:wght@400;600&display=swap" rel="stylesheet">
<style>
  :root {
    --red: #d32129;
    --blue: #2299d5;
    --navy: #2b5970;
    --coral: #e5575c;
    --orange: #e48457;
    --gold: #e3b655;
    --ink: #1d1d1b;
    --slate: #4a4a4a;
    --blush: #fbe4e6;
    --white: #ffffff;
  }
  * { margin: 0; padding: 0; box-sizing: border-box; }
  html, body { width: 1200px; height: 720px; overflow: hidden; background: var(--white); }
  .canvas { position: relative; width: 1200px; height: 720px; font-family: "Nunito Sans", sans-serif; color: var(--ink); }
  .strategy-diagram { position: absolute; inset: 0; }
  .headline {
    position: absolute; top: 30px; left: 0; width: 1200px; text-align: center;
    font-family: "Arimo", sans-serif; font-weight: 700; font-style: italic;
    font-size: 16.5px; color: var(--red);
  }
  .headline .org { font-style: normal; }
  .info-card {
    position: absolute; width: 282px; background: var(--white);
    border-radius: 4px 4px 16px 16px; box-shadow: 0 2px 6px rgba(0,0,0,0.18);
    overflow: hidden;
  }
  .info-card__title {
    background: var(--red); color: var(--white); text-align: center;
    font-family: "Arimo", sans-serif; font-weight: 700; font-size: 13.5px;
    letter-spacing: 0.2px; line-height: 16.5px; display: flex; align-items: center; justify-content: center;
  }
  .info-card__list { list-style: none; padding: 14px 12px 0 17px; font-size: 14px; line-height: 17px; }
  .info-card__list li { position: relative; padding-left: 8px; margin-bottom: 2.6px; }
  .info-card__list li::before { content: "•"; position: absolute; left: -2px; top: 0; font-size: 10px; }
  .card-frameworks { left: 44px; top: 81px; height: 160px; }
  .card-values { left: 866px; top: 81px; height: 160px; }
  .card-knowledge { left: 44px; top: 527px; height: 121px; }
  .card-outcome { left: 866px; top: 527px; height: 121px; }
  .card-frameworks .info-card__title, .card-values .info-card__title { height: 35px; }
  .card-knowledge .info-card__title { height: 53px; }
  .card-outcome .info-card__title { height: 35px; }
  .card-knowledge .info-card__list, .card-outcome .info-card__list { padding-top: 16px; }
  .label-ring { font-family: "Arimo", sans-serif; font-weight: 700; fill: var(--white); font-size: 12px; }
  .label-outer { font-family: "Arimo", sans-serif; font-weight: 700; fill: var(--slate); font-size: 15.5px; }
  .label-hub { font-family: "Arimo", sans-serif; font-weight: 700; fill: var(--slate); font-size: 11.5px; }
  .label-pillar { font-family: "Arimo", sans-serif; font-weight: 700; fill: var(--white); font-size: 16px; }
  .brand-name { font-family: "Nunito Sans", sans-serif; font-weight: 600; fill: var(--slate); font-size: 11px; }
  .icon { fill: none; stroke: var(--white); stroke-width: 2.2; stroke-linecap: round; stroke-linejoin: round; }
</style>
</head>
<body>
<div class="canvas">
  <svg class="strategy-diagram" width="1200" height="720" viewBox="0 0 1200 720" xmlns="http://www.w3.org/2000/svg">
    <defs>
      <radialGradient id="worldTint" cx="50%" cy="50%" r="60%">
        <stop offset="0%" stop-color="#fae3e5" stop-opacity="0.85"/>
        <stop offset="100%" stop-color="#fdf3f4" stop-opacity="0.4"/>
      </radialGradient>
    </defs>

    <rect class="world-map" role="img" aria-label="Faint world map in the background" x="150" y="68" width="980" height="632" rx="160" fill="url(#worldTint)"/>

    <!-- flow loop -->
    <ellipse cx="600" cy="379" rx="373" ry="300" fill="none" stroke="var(--blue)" stroke-width="12"/>
    <polygon points="207,272 255,276 227,314" fill="var(--blue)"/>
    <polygon points="967,442 993,484 944,482" fill="var(--blue)"/>

    <!-- pillars -->
    <circle cx="227" cy="378" r="64" fill="var(--red)"/>
    <text class="label-pillar" x="227" y="376" text-anchor="middle">GLOBAL</text>
    <text class="label-pillar" x="227" y="393" text-anchor="middle">POLICY</text>
    <circle cx="975" cy="378" r="64" fill="var(--red)"/>
    <text class="label-pillar" x="975" y="376" text-anchor="middle">LOCAL</text>
    <text class="label-pillar" x="975" y="393" text-anchor="middle">ACTION</text>

    <!-- activity wheel -->
    <g class="activity-wheel" stroke="var(--blush)" stroke-width="5">
      <path d="M601.8,169 A218,218 0 0 1 808.6,330.6 L704.2,358.5 A110,110 0 0 0 599.9,277 Z" fill="var(--navy)"/>
      <path d="M808.6,330.6 A218,218 0 0 1 723,565.6 L661.1,477.1 A110,110 0 0 0 704.2,358.5 Z" fill="var(--blue)"/>
      <path d="M723,565.6 A218,218 0 0 1 438.6,535.7 L517.5,462 A110,110 0 0 0 661.1,477.1 Z" fill="var(--gold)"/>
      <path d="M438.6,535.7 A218,218 0 0 1 390.7,319.6 L493.4,353 A110,110 0 0 0 517.5,462 Z" fill="var(--orange)"/>
      <path d="M390.7,319.6 A218,218 0 0 1 601.8,169 L599.9,277 A110,110 0 0 0 493.4,353 Z" fill="var(--coral)"/>
    </g>
    <circle cx="598" cy="387" r="104" fill="var(--blush)"/>
    <g fill="none" stroke-width="9">
      <path d="M602,297 A90,90 0 0 1 683,361" stroke="var(--navy)"/>
      <path d="M686,367 A90,90 0 0 1 652,458" stroke="var(--blue)"/>
      <path d="M646,463 A90,90 0 0 1 536,451" stroke="var(--gold)"/>
      <path d="M530,445 A90,90 0 0 1 513,364" stroke="var(--orange)"/>
      <path d="M515,356 A90,90 0 0 1 594,297" stroke="var(--coral)"/>
    </g>
    <circle cx="598" cy="387" r="80" fill="var(--white)"/>

    <!-- hub -->
    <text class="brand-name" x="600" y="384" text-anchor="middle">Brightwell Circle OKAV</text>
    <text class="label-hub" x="604" y="420" text-anchor="middle">NETWORK OF</text>
    <text class="label-hub" x="604" y="435" text-anchor="middle">NETWORKS</text>

    <!-- icons -->
    <g class="icon">
      <circle cx="545" cy="230" r="15"/><line x1="545" y1="245" x2="545" y2="266"/>
      <ellipse cx="545" cy="230" rx="22" ry="9" transform="rotate(35 545 230)"/>
      <ellipse cx="545" cy="230" rx="22" ry="9" transform="rotate(-35 545 230)"/>

      <polyline points="677,232 677,286 733,286"/>
      <circle cx="705" cy="258" r="17"/><line x1="693" y1="270" x2="680" y2="292"/>
      <polyline points="694,262 701,254 708,262 718,251"/>

      <path d="M734,432 a18,18 0 1 1 18,0 l-2,20 h-14 z"/>
      <line x1="737" y1="458" x2="749" y2="458"/><line x1="738" y1="464" x2="748" y2="464"/>
      <polyline points="737,412 743,430 749,412"/>

      <circle cx="440" cy="385" r="25"/><line x1="458" y1="403" x2="478" y2="427"/>
      <rect x="427" y="380" width="27" height="17" rx="2"/><path d="M435,380 v-5 h11 v5"/>

      <circle cx="591" cy="527" r="8"/>
      <circle cx="591" cy="527" r="16" stroke-dasharray="5 3"/>
      <path d="M565,527 a26,26 0 0 1 44,-19"/><path d="M617,527 a26,26 0 0 1 -44,19"/>
    </g>

    <!-- segment labels -->
    <text class="label-ring" x="486" y="260" text-anchor="middle">REGIONAL</text>
    <text class="label-ring" x="486" y="274" text-anchor="middle">MEETINGS</text>
    <text class="label-ring" x="726" y="318" text-anchor="middle">TASKFORCES</text>
    <text class="label-ring" x="735" y="496" text-anchor="middle">CONFERENCES</text>
    <text class="label-ring" x="591" y="579" text-anchor="middle">SYMPOSIUMS</text>
    <text class="label-ring" x="456" y="462" text-anchor="middle">WORKSHOPS</text>

    <!-- outputs -->
    <text class="label-outer" x="599" y="146" text-anchor="middle">PUBLICATIONS</text>
    <text class="label-outer" x="339" y="310" text-anchor="middle">POLICY</text>
    <text class="label-outer" x="339" y="327" text-anchor="middle">PAPERS</text>
    <text class="label-outer" x="764" y="598" text-anchor="middle">TRAINING</text>
    <text class="label-outer" x="764" y="615" text-anchor="middle">CURRICULA</text>
  </svg>

  <h1 class="headline"><span class="org">OKAV</span> drives is work through Global and Regional Partnerships</h1>

  <section class="info-card card-frameworks">
    <h2 class="info-card__title">FRAMEWORKS</h2>
    <ul class="info-card__list">
      <li>Social Accountability &amp; Accreditation</li>
      <li>Interprofessional Education &amp; Team - based Care</li>
      <li>Population Health</li>
    </ul>
  </section>

  <section class="info-card card-values">
    <h2 class="info-card__title">GUIDING VALUES</h2>
    <ul class="info-card__list">
      <li>Community Relevance</li>
      <li>Informed Consumer</li>
      <li>Patient / Consumer Voice</li>
      <li>Intersectoral, multi disciplinary</li>
    </ul>
  </section>

  <section class="info-card card-knowledge">
    <h2 class="info-card__title">NETWORK KNOWLEDGE<br>BEST PRACTICES</h2>
    <ul class="info-card__list">
      <li>Remote/Rural, Women, Migrants, Refugees, Indigenous Health</li>
    </ul>
  </section>

  <section class="info-card card-outcome">
    <h2 class="info-card__title">OUTCOME</h2>
    <ul class="info-card__list">
      <li>Coordinated Action by Local Change Agents and Networks</li>
    </ul>
  </section>
</div>
</body>
</html>
```